hi all

Im after a new age looking business card with my company logo on it

must include these details, I would like the PH and Email to be symbols

If the colours used for card could be kept within the colours used in logo that I have supplied that would be great, if another colour is to be used dark grey would be ok. no light bulbs etc thanks

Details below to be incorporated on card

Damian Holloway

Lic E871302

PH 0219647381

E info@brightvaleelectrical.example.nz

Domestic Commercial Industrial Electricians

```html
<!DOCTYPE html>
<html lang="en">
<head>
<meta charset="utf-8">
<title>Brightvale Electrical – Business Card</title>
<link rel="stylesheet" href="https://fonts.googleapis.com/css2?family=Open+Sans:wght@400;600;700&display=swap">
<style>
  :root {
    --bg: #e9e6e1;
    --card-black: #0d0d0d;
    --card-white: #ffffff;
    --brand-blue: #1b75bc;
    --text-dark: #3a3a3a;
    --font-main: "Open Sans", Arial, sans-serif;
  }
  html, body {
    margin: 0;
    padding: 0;
    width: 1200px;
    height: 900px;
    overflow: hidden;
    background: var(--bg);
    font-family: var(--font-main);
  }
  .stage {
    position: relative;
    width: 1200px;
    height: 900px;
  }
  .card {
    position: absolute;
    left: 280px;
    width: 640px;
    height: 390px;
    overflow: hidden;
    box-shadow: 0 6px 18px rgba(0,0,0,0.18);
  }
  /* Back of card */
  .card-back {
    top: 40px;
    background: var(--card-black);
    display: flex;
    align-items: center;
    justify-content: center;
  }
  .brand {
    display: flex;
    align-items: center;
    gap: 18px;
  }
  .brand-dot {
    width: 54px;
    height: 54px;
    border-radius: 50%;
    flex: none;
  }
  .brand-name {
    font-weight: 700;
    line-height: 1;
    text-transform: uppercase;
  }
  .brand-name .line-main { display: block; font-size: 58px; letter-spacing: 2px; }
  .brand-name .line-sub { display: block; font-size: 17px; letter-spacing: 7px; text-align: right; margin-top: 6px; }
  .card-back .brand-dot { background: var(--card-white); }
  .card-back .brand-name { color: var(--card-white); }

  /* Front of card */
  .card-front {
    top: 470px;
    background: var(--card-white);
  }
  .card-front .wave {
    position: absolute;
    inset: 0;
  }
  .holder-name {
    position: absolute;
    left: 48px;
    top: 62px;
    margin: 0;
    font-size: 22px;
    font-weight: 700;
    letter-spacing: 1px;
    color: var(--brand-blue);
    text-transform: uppercase;
  }
  .licence {
    position: absolute;
    left: 58px;
    top: 104px;
    margin: 0;
    font-size: 18px;
    color: var(--text-dark);
  }
  .licence .label { color: var(--brand-blue); }
  .card-front .brand {
    position: absolute;
    right: 44px;
    top: 48px;
    gap: 12px;
  }
  .card-front .brand-dot { width: 36px; height: 36px; background: var(--brand-blue); }
  .card-front .brand-name { color: var(--brand-blue); }
  .card-front .brand-name .line-main { font-size: 36px; letter-spacing: 1px; }
  .card-front .brand-name .line-sub { font-size: 11px; letter-spacing: 5px; margin-top: 4px; color: var(--brand-blue); }
  .contact {
    position: absolute;
    left: 52px;
    top: 212px;
    margin: 0;
    padding: 0;
    list-style: none;
    font-size: 16px;
    color: var(--text-dark);
  }
  .contact li {
    display: flex;
    align-items: center;
    gap: 8px;
    height: 26px;
  }
  .contact svg { width: 18px; height: 18px; flex: none; }
  .tagline {
    position: absolute;
    right: 40px;
    bottom: 30px;
    margin: 0;
    font-size: 14px;
    letter-spacing: 0.6px;
    color: var(--card-white);
    text-transform: uppercase;
  }
</style>
</head>
<body>
<main class="stage">

  <section class="card card-back" aria-label="Card back">
    <div class="brand">
      <span class="brand-dot"></span>
      <div class="brand-name">
        <span class="line-main">Brightvale</span>
        <span class="line-sub">Electrical</span>
      </div>
    </div>
  </section>

  <section class="card card-front" aria-label="Card front">
    <svg class="wave" viewBox="0 0 640 390" preserveAspectRatio="none" aria-hidden="true">
      <path d="M40,296 C230,312 400,258 540,188 C420,268 240,318 40,304 Z" fill="var(--brand-blue)"/>
      <path d="M0,318 C220,350 440,272 640,160 L640,390 L0,390 Z" fill="var(--card-black)"/>
    </svg>

    <h1 class="holder-name">Damian Holloway</h1>
    <p class="licence"><span class="label">Lic</span> E871302</p>

    <div class="brand">
      <span class="brand-dot"></span>
      <div class="brand-name">
        <span class="line-main">Brightvale</span>
        <span class="line-sub">Electrical</span>
      </div>
    </div>

    <ul class="contact">
      <li>
        <svg viewBox="0 0 18 18" aria-label="Phone">
          <rect x="1" y="1" width="16" height="16" rx="3" fill="none" stroke="var(--brand-blue)" stroke-width="1.6"/>
          <path d="M6,4.5 L7.6,6.6 L6.8,7.6 C7.5,9 8.8,10.4 10.3,11.2 L11.3,10.4 L13.5,12 L12.4,13.6 C8.6,13.2 4.8,9.4 4.4,5.6 Z" fill="var(--brand-blue)"/>
        </svg>
        0219647381
      </li>
      <li>
        <svg viewBox="0 0 18 18" aria-label="Email">
          <rect x="1" y="3.5" width="16" height="11" fill="var(--brand-blue)"/>
          <path d="M1.5,4 L9,10 L16.5,4" fill="none" stroke="var(--card-white)" stroke-width="1.3"/>
        </svg>
        info@brightvaleelectrical.example.nz
      </li>
    </ul>

    <p class="tagline">Domestic Commercial Industrial Electricians</p>
  </section>

</main>
</body>
</html>
```